Quill|Marlow & Petrie business card contest

We need a logo for an upscale boutique diversified company involved in real estate, investments, cattle, and more. Our businesses DO NOT need to be reflected in the business card nor do we want them noted. This is our logo and colors and we love our logo and colors. Our logo looks best against a black background and we like to include the firm name in our logo usage. importantly, the names Quill and Marlow are separated by | not / and we use an ampersand not the word and.
On the front of the card, we want to include:
company logo and name (Quill|Marlow & Petrie)
on the back, we would definitely include:
address, email, cell #
logo and name (smaller size than front)

The variable will be location of individual name and title (mine for example is ) - whether on the front OR on the back. interested in variations from which to choose
Dr. Owen T. Caldecott, CFA
Scientifique des Fusées Financières

we would like to use contemporary symbols for address, email address, cell # with an option for web site that we do not intend to use initially. we like two sided cards and believe this design should use four rounded corners with the standard size. we prefer thicker card stock and may look at metal.

```html
<!DOCTYPE html>
<html lang="en">
<head>
<meta charset="utf-8">
<title>Quill|Marlow &amp; Petrie – Business Card</title>
<link href="https://fonts.googleapis.com/css2?family=Roboto:ital,wght@0,400;0,500;1,400&display=swap" rel="stylesheet">
<style>
  :root {
    --page-bg: #3a3a3a;
    --card-edge: #8a8a8c;
    --card-light: #ececee;
    --card-mid: #c9c9cb;
    --card-dark: #7c7c7e;
    --accent: #c8600e;
    --ink: #2e2e30;
    --ink-soft: #555557;
    --rule: #555557;
  }
  * { margin: 0; padding: 0; box-sizing: border-box; }
  html, body {
    width: 1125px; height: 1200px; overflow: hidden;
    background: var(--page-bg);
    font-family: "Roboto", Arial, sans-serif;
  }
  .card {
    position: absolute;
    left: 177px;
    width: 824px;
    height: 470px;
    border-radius: 26px;
    overflow: hidden;
  }
  .card--front {
    top: 106px;
    background: linear-gradient(to bottom, var(--card-dark) 0%, var(--card-mid) 25%, var(--card-light) 48%, var(--card-mid) 75%, var(--card-dark) 100%);
  }
  .card--back {
    top: 640px;
    background: linear-gradient(to bottom, var(--card-dark) 0%, var(--card-mid) 50%, var(--card-dark) 100%);
    border: 2px solid var(--card-edge);
  }
  .brand {
    position: absolute;
    display: flex; align-items: center; gap: 14px;
    color: var(--ink-soft);
    font-weight: 400;
    white-space: nowrap;
  }
  .brand__square { background: var(--accent); flex: none; }
  .card--front .brand { left: 59px; top: 150px; font-size: 30px; }
  .card--front .brand__square { width: 22px; height: 22px; }
  .card--back .brand {
    left: 0; right: 0; top: 215px; justify-content: center;
    font-size: 46px; color: #4a4a4c; gap: 20px;
  }
  .card--back .brand__square { width: 34px; height: 34px; }

  .person { position: absolute; left: 59px; top: 244px; }
  .person__name { color: var(--accent); font-weight: 500; font-size: 26px; line-height: 1; }
  .person__name small { font-size: 17px; }
  .person__title { color: var(--ink-soft); font-style: italic; font-size: 17px; margin-top: 6px; }

  .rule { position: absolute; left: 59px; width: 512px; height: 2px; background: var(--rule); }
  .rule--top { top: 320px; }
  .rule--bottom { top: 392px; }

  .contact {
    position: absolute; left: 59px; top: 331px;
    display: grid; grid-template-columns: 246px auto;
    font-size: 18px; line-height: 24px; color: var(--ink);
  }
  .web {
    position: absolute; color: var(--ink);
    letter-spacing: 3.6px;
  }
  .card--front .web { left: 59px; top: 405px; font-size: 18px; }
  .card--back .web {
    left: 0; right: 0; text-align: center; top: 406px;
    font-style: italic; font-size: 17px; letter-spacing: 2.6px; color: #111;
  }
</style>
</head>
<body>
  <section class="card card--front" aria-label="Card front">
    <div class="brand"><span class="brand__square"></span>Quill|Marlow &amp; Petrie</div>
    <div class="person">
      <p class="person__name"><small>Dr.</small> Owen T. Caldecott, <small>CFA</small></p>
      <p class="person__title">Scientifique des Fusées Financières</p>
    </div>
    <div class="rule rule--top"></div>
    <div class="contact">
      <span>4210 Alder Crest Road</span><span>Mob- 907-555-0148</span>
      <span>Juneau, Alaska 99801</span><span>info@quillmarlowpetrie.com</span>
    </div>
    <div class="rule rule--bottom"></div>
    <p class="web">www.quillmarlowpetrie.com</p>
  </section>

  <section class="card card--back" aria-label="Card back">
    <div class="brand"><span class="brand__square"></span>Quill|Marlow &amp; Petrie</div>
    <p class="web">www.quillmarlowpetrie.com</p>
  </section>
</body>
</html>
```